Website redesign for fast growing company looking to present a unique image

We're looking to revamp our online image to represent the professional, accomplished company we have become. We want to move beyond a templated look and feel to a custom design - we are eager to have you design a new public face for us! In particular, we need creative ways to display text to stand out. We are reaching top-level, C-suite executives and want to give them the confidence that we have the skills, talent, expertise, and knowledge to help their companies grow.
Updates

Designs look the same

Target Market(s)

contact centers, business process outsourcing

Industry/Entity Type

Call Center

Coding

Coded - Design and coding required

Number of Pages Required

4 page

Font styles to use
Sans Serif

Colors

Designer to choose colors to be used in the design.

Requirements
Must have
• Designed for a professional audience - C-suite executives - but that also shows our personality as a company that is nimble, personable, trustworthy, and smart. Must be lively, but not quirky. Professional, but not overly formal. Be bold with choices for imagery - we want to look unique so go beyond traditional "business/corporate" stock photos. Instead use imagery similar to what is on our staging website - torvenda.com/staging. Do not use the "neon" sign. Use colors to match and complement our logo - bright orange and dark blue. Creative text boxes that we can use throughout the site. I have attached pages of our current staging site to display some of the types of imagery that might work. We are looking for "professional with a personality" Note: this design will be transferred into a Wordpress framework.
Nice to have
• We like the animated text features of the Vorquin.com site - bold colors, great display of text features that break up the page and engage people to continue scrolling.
Should not have
• Cheesy stock photos of call center agents wearing headsets. Overly used stock photos of professionals in suits shaking hands, high-rise buildings, connection/network graphics. Current management does not like the neon sign graphics displayed on our staging site (torvenda.com/staging). We do not like style of sites that use cartoon-like icons and figures.

```html
<!DOCTYPE html>
<html lang="en">
<head>
<meta charset="utf-8">
<title>Torvenda — Contact Center Experts</title>
<link href="https://fonts.googleapis.com/css2?family=Poppins:wght@300;400;500;600&display=swap" rel="stylesheet">
<style>
:root{
  --navy:#24476b;
  --orange:#f0562a;
  --ink:#111418;
  --muted:#8a8f96;
  --soft:#fafafa;
  --white:#ffffff;
}
*{margin:0;padding:0;box-sizing:border-box}
html,body{width:1200px;height:2445px;overflow:hidden}
body{font-family:'Poppins',sans-serif;color:var(--ink);background:var(--white)}
.wrap{width:878px;margin:0 auto;position:relative}

.topbar{height:38px;background:var(--navy);color:var(--white);font-size:12px}
.topbar .wrap{height:100%;display:flex;justify-content:flex-end;align-items:center;gap:14px}
.topbar .phone-dot{width:24px;height:24px;border-radius:50%;background:var(--white);display:flex;align-items:center;justify-content:center}
.topbar .number{font-weight:500}

.header{height:74px;background:var(--white)}
.header .wrap{height:100%;display:flex;align-items:center;justify-content:space-between}
.brand{color:var(--orange);font-size:34px;font-weight:500;letter-spacing:-0.5px}
.nav{display:flex;align-items:center;gap:28px;font-size:10.5px;color:#7a7f86;height:100%}
.nav a{color:inherit;text-decoration:none;height:100%;display:flex;align-items:center;position:relative}
.nav a.active{color:var(--orange)}
.nav a.active::after{content:"";position:absolute;left:0;right:0;bottom:0;height:3px;background:var(--orange)}

.hero{height:600px;position:relative;background:linear-gradient(90deg,#5d5c5a 0%,#807466 40%,#a27550 58%,#8a8780 80%,#6f6e6b 100%)}
.hero .wrap{padding-top:144px;color:var(--white)}
.hero h1{font-size:48px;font-weight:600;line-height:49px;letter-spacing:0.3px}
.hero h1 span{color:var(--orange)}
.hero p{font-size:15.5px;font-weight:300;line-height:26px;margin-top:20px;width:370px}
.btn{display:inline-block;background:var(--orange);color:var(--white);font-size:12.5px;border-radius:24px;padding:0 22px;height:45px;line-height:45px;text-decoration:none}
.hero .btn{margin-top:22px}

.intro{height:285px;text-align:center;padding-top:55px}
.intro h2,.services h2,.closing h2{font-size:31px;font-weight:600}
.lede{font-size:12px;color:var(--muted);line-height:20px;font-weight:300;margin:18px auto 0}
.intro .lede{width:600px}
.down{width:30px;height:30px;border-radius:50%;background:var(--orange);margin:24px auto 0;display:flex;align-items:center;justify-content:center}

.services{height:375px;background:var(--soft);text-align:center;padding-top:58px}
.services .lede{width:340px}
.service-list{display:flex;justify-content:space-between;margin-top:38px}
.service{width:200px;text-align:center}
.service .icon{width:75px;height:75px;border-radius:50%;background:var(--navy);margin:0 auto;display:flex;align-items:center;justify-content:center}
.service.featured .icon{background:var(--orange)}
.service h3{font-size:15.5px;font-weight:500;line-height:23px;margin-top:15px}
.service.featured h3{color:var(--orange)}

.benefits{height:403px}
.benefits .wrap{display:flex;justify-content:space-between;padding-top:60px}
.benefits h2{font-size:31px;font-weight:600;line-height:34px;width:400px}
.benefits ul{list-style:none;margin-top:26px}
.benefits li{font-size:13px;color:var(--muted);font-weight:300;line-height:26.3px}
.benefits li b{color:var(--orange);font-weight:400}
.visual{position:relative;width:382px;height:284px;margin-top:1px;margin-right:0}
.visual .accent{position:absolute;left:22px;top:22px;width:360px;height:262px;background:var(--orange)}
.visual .photo{position:absolute;left:0;top:0;width:359px;height:262px;background:linear-gradient(135deg,#3a3532 0%,#5a524b 45%,#8a7a6a 70%,#5e4732 100%)}

.closing{height:257px;background:var(--soft);text-align:center;padding-top:60px}
.closing .lede{margin-top:14px}
.closing .btn{margin-top:22px;padding:0 24px}

.footer{height:346px;background:var(--navy);text-align:center;color:var(--white);padding-top:58px}
.footer .brand{font-size:44px}
.footer .address{font-size:14px;margin-top:30px}
.social{display:flex;justify-content:center;gap:8px;margin-top:18px}
.social span{width:30px;height:30px;border-radius:50%;background:var(--white)}
.links{width:760px;margin:22px auto 0;font-size:11px;line-height:19px;color:#b7c3d1;font-weight:300}
.links i{font-style:normal;margin:0 8px}

.copyright{height:67px;background:var(--navy);border-top:1px solid #35587b;color:var(--white);font-size:9px;text-align:center;line-height:66px}
</style>
</head>
<body>

<div class="topbar">
  <div class="wrap">
    <span>Call Us Now</span>
    <span class="phone-dot">
      <svg width="12" height="12" viewBox="0 0 24 24"><path fill="#f0562a" d="M6.6 10.8a15.1 15.1 0 0 0 6.6 6.6l2.2-2.2c.3-.3.7-.4 1-.2 1.1.4 2.3.6 3.6.6.6 0 1 .4 1 1V20c0 .6-.4 1-1 1A17 17 0 0 1 3 4c0-.6.4-1 1-1h3.5c.6 0 1 .4 1 1 0 1.3.2 2.5.6 3.6.1.3 0 .7-.2 1z"/></svg>
    </span>
    <span class="number">+1 555.014.2290</span>
  </div>
</div>

<header class="header">
  <div class="wrap">
    <div class="brand">Torvenda</div>
    <nav class="nav">
      <a class="active" href="#">HOME</a>
      <a href="#">MARKETS WE SERVE</a>
      <a href="#">ABOUT US</a>
      <a href="#">APPLY TODAY</a>
      <a href="#">CONTACT</a>
      <svg width="17" height="17" viewBox="0 0 24 24" fill="none" stroke="#555" stroke-width="2"><circle cx="10" cy="10" r="7"/><path d="M15 15l6 6"/></svg>
    </nav>
  </div>
</header>

<section class="hero" role="img" aria-label="Smiling man in an orange shirt with arms crossed in a bright office">
  <div class="wrap">
    <h1>Get More from<br>Your <span>Customer<br>Interactions</span></h1>
    <p>Lift Your Top and Bottom Lines with Professional Outsourcing Solutions from Torvenda</p>
    <a class="btn" href="#">APPLY TODAY</a>
  </div>
</section>

<section class="intro">
  <h2>It’s A New World. Are You Ready?</h2>
  <p class="lede">It's time to find solutions that deliver more value. Shed the manual interactions that cost you money and distract you from your core. Get more by partnering with Torvenda for Customer Service, Tech Support, and Business Process Outsourcing solutions.</p>
  <div class="down"><svg width="14" height="14" viewBox="0 0 24 24" fill="none" stroke="#fff" stroke-width="2"><path d="M6 6l6 6 6-6M6 12l6 6 6-6"/></svg></div>
</section>

<section class="services">
  <div class="wrap">
    <h2>What We Do</h2>
    <p class="lede">Flexible, versatile, end-to-end outsourcing options to help you get more of what your business needs.</p>
    <div class="service-list">
      <div class="service">
        <div class="icon"><svg width="36" height="36" viewBox="0 0 24 24" fill="none" stroke="#fff" stroke-width="1.4"><rect x="3" y="4" width="18" height="12" rx="2"/><path d="M8 20h8M12 16v4"/></svg></div>
        <h3>Customer Service<br>Contact Center</h3>
      </div>
      <div class="service featured">
        <div class="icon"><svg width="36" height="36" viewBox="0 0 24 24" fill="none" stroke="#fff" stroke-width="1.4"><circle cx="12" cy="12" r="3"/><path d="M12 2v3M12 19v3M2 12h3M19 12h3M4.9 4.9l2.1 2.1M17 17l2.1 2.1M4.9 19.1L7 17M17 7l2.1-2.1"/></svg></div>
        <h3>Tech Support<br>Service Center</h3>
      </div>
      <div class="service">
        <div class="icon"><svg width="36" height="36" viewBox="0 0 24 24" fill="none" stroke="#fff" stroke-width="1.4"><path d="M4 20V10M10 20V4M16 20v-7M22 20H2"/></svg></div>
        <h3>Business Process<br>Outsourcing</h3>
      </div>
      <div class="service">
        <div class="icon"><svg width="36" height="36" viewBox="0 0 24 24" fill="none" stroke="#fff" stroke-width="1.4"><circle cx="12" cy="12" r="9"/><path d="M7.5 12l3 3 6-6"/></svg></div>
        <h3>End-to-End Solutions</h3>
      </div>
    </div>
  </div>
</section>

<section class="benefits">
  <div class="wrap">
    <div class="benefits-text">
      <h2>Discover the Benets of Outsourcing</h2>
      <ul>
        <li><b>Shed overhead</b> and invest in core resources.</li>
        <li><b>Reduce risk</b> – Lower headcount, infrastructure, and technology costs.</li>
        <li><b>Scale up and down</b> as needed.</li>
        <li><b>Focus on your business,</b> not on labor-intensive processes.</li>
        <li><b>Build customer anity</b> with professional service teams.</li>
        <li><b>Continuous improvement</b> via performance management.</li>
        <li><b>Access data</b> to make better business decisions.</li>
      </ul>
    </div>
    <div class="visual">
      <div class="accent"></div>
      <div class="photo" role="img" aria-label="Woman with long hair reading a tablet at a wooden table"></div>
    </div>
  </div>
</section>

<section class="closing">
  <h2>Better. Faster. Leaner. Smarter</h2>
  <p class="lede">Get More from Your Customer Interactions</p>
  <a class="btn" href="#">LEARN MORE</a>
</section>

<footer class="footer">
  <div class="brand">Torvenda</div>
  <p class="address">18 Halden Street Unit 4, Suite 210 Marlow, ME 04990</p>
  <div class="social"><span></span><span></span><span></span><span></span></div>
  <p class="links">Contac<i>|</i>Leadership Team<i>|</i>Company Overview<i>|</i>Government Services<i>|</i>Tech Support Contact Center<i>|</i>Customer Service for eCommerce<i>|</i>Healthcare &amp; Insurance<i>|</i>Customer Service Contact Center<i>|</i>Business Process Outsourcing<i>|</i>Tech Support Contact Center<i>|</i>Career Opportunities<i>|</i>Analytics for Contact Centers<i>|</i>Email Us</p>
</footer>
<div class="copyright">Copyright © TORVENDA CONTACT CENTER EXPERT - 2020 . All Right Reserved.</div>

</body>
</html>
```